WP website design (Brenn)

We need a wordpress design for an established auction and real estate company based in Tennessee. The winning design will incorporate a professional color scheme with company logo in a clean layout. The design needs to consider that this will be developed on a responsive theme. Colors are those that will highlight the logo.

Industry/Entity Type

Real Estate

Font styles to use
Sans Serif

Colors

Designer to choose colors to be used in the design.

Requirements
Must have
• Navigation: 1) Home - with auctions as content as seen at http://vornelbidhouse.com/ 2) Current Auctions 3) Past Auctions 4) Referrals 5) Why Auction 6) About Us 7) Contact Us

Header will have logo, contact info, Social icons (Facebook, Twitter, Youtube) and tagline "Bid Smart With Brenn!' Slideshow (use stock real estate image for image) will be used either in header or content area.

Widgets: Email signup form, Upcoming Auctions, Register for Online Bidding text, testimonials

Footer will have contact info (below) smaller company logo, and the association logos attached.

```html
<!DOCTYPE html>
<html lang="en">
<head>
<meta charset="utf-8">
<title>Brenn Realty &amp; Auction LLC</title>
<link rel="stylesheet" href="https://fonts.googleapis.com/css2?family=Source+Sans+3:wght@400;600&family=Arimo:ital,wght@0,400;0,700;1,700&display=swap">
<style>
:root{
  --green:#6a8f3c;
  --green-dark:#4f7a2a;
  --navy:#353a5c;
  --ink:#222;
  --muted:#444;
  --panel:#f2f2f2;
  --line:#d6d6d6;
  --footer:#3b3b3b;
  --footer-base:#262626;
}
*{box-sizing:border-box;margin:0;padding:0}
html,body{width:806px;height:1200px;overflow:hidden;background:#fff}
body{position:relative;font-family:"Arimo",Arial,sans-serif;color:var(--ink)}
.head{font-family:"Source Sans 3",Arial,sans-serif}
.abs{position:absolute}

/* header */
.brand{left:67px;top:12px;display:flex;align-items:center;gap:8px}
.brand-mark{width:14px;height:14px;background:var(--green)}
.brand-name{font-family:"Source Sans 3",sans-serif;font-weight:600;font-size:22px;color:var(--navy);line-height:1.05}
.social{right:67px;top:17px;display:flex;align-items:center;gap:13px}
.social-label{font-family:"Source Sans 3",sans-serif;font-size:16px;color:#333;letter-spacing:.5px;margin-right:-3px}
.social-btn{width:26px;height:26px;display:block}
.contact{right:67px;top:56px;font-family:"Source Sans 3",sans-serif;font-size:12.5px;color:#333;display:flex;align-items:center;gap:5px}
.contact svg{display:block}

/* nav */
.nav{left:0;top:86px;width:806px;height:34px;background:var(--green);display:flex;align-items:center;padding-left:71px}
.nav a{font-family:"Source Sans 3",sans-serif;font-size:10.5px;color:#fff;text-decoration:none;text-transform:uppercase;padding:4px 8px;position:relative}
.nav a.active{background:var(--navy)}
.nav .sep{width:1px;height:22px;background:#86a85b}

/* hero */
.hero{left:0;top:120px;width:806px;height:306px;background:linear-gradient(180deg,#d9e4ec 0%,#a9b2ae 38%,#7f8579 62%,#4f6d35 82%,#6f5a4c 100%)}
.tagline{left:378px;top:233px;width:361px;height:47px;background:rgba(40,40,40,.72);color:#fff;font-family:"Source Sans 3",sans-serif;font-size:33px;line-height:47px;text-align:center}

/* welcome */
.welcome-title{left:71px;top:449px;font-size:20px;line-height:26px;color:var(--green);font-weight:400}
.welcome-text{left:72px;top:481px;width:442px;font-size:9px;line-height:13.5px;color:var(--ink)}
.section-title{left:68px;top:539px;font-size:20px;font-weight:400;color:#444}

/* auction cards */
.card{left:68px;width:441px;height:157px;background:linear-gradient(180deg,#fbfbfb,#ececec);border:1px solid var(--line)}
.card-head{position:absolute;left:4px;top:4px;right:4px;height:24px;background:var(--navy);color:#fff;font-size:12px;line-height:24px;padding-left:10px}
.card-photo{position:absolute;left:10px;top:44px;width:117px;height:68px;background:linear-gradient(180deg,#c9d7e2 0%,#3d5049 55%,#4c7a34 100%);border:2px solid #ddd}
.card-btn{position:absolute;left:33px;top:121px;width:72px;height:20px;background:var(--green-dark);border:1px solid #3f6421;border-radius:2px;color:#fff;font-size:9.5px;font-weight:700;display:flex;align-items:center;justify-content:center;gap:5px}
.card-body{position:absolute;left:135px;top:44px;width:296px;font-size:9px;line-height:12px;color:#333}
.card-body .label{color:var(--green);font-weight:700;margin-top:3px}
.card-body .label:first-child{margin-top:0}
.card-body p{text-align:justify}

/* sidebar */
.email{left:533px;top:450px;width:206px;height:107px;background:var(--navy);color:#fff;padding:10px 13px}
.email h3{font-family:"Source Sans 3",sans-serif;font-weight:400;font-size:19px;letter-spacing:.4px}
.email p{font-size:8.5px;line-height:12px;margin-top:5px}
.email-form{display:flex;margin-top:8px}
.email-input{width:146px;height:23px;background:#fff;font-size:8px;color:#999;line-height:23px;padding-left:6px}
.email-go{width:32px;height:23px;background:var(--green-dark);font-family:"Source Sans 3",sans-serif;font-size:13px;line-height:23px;text-align:center}

.register{left:533px;top:574px;width:206px;height:78px;background:var(--green);color:#fff}
.register .big{left:59px;top:8px;font-family:"Source Sans 3",sans-serif;font-weight:600;font-size:32px;line-height:36px;letter-spacing:.5px}
.register .small{left:60px;top:46px;font-family:"Source Sans 3",sans-serif;font-size:13.5px;letter-spacing:.7px}

.widget{left:533px;width:206px;background:var(--panel);border:1px solid var(--line);padding:10px 16px}
.widget h3{font-family:"Source Sans 3",sans-serif;font-weight:600;font-size:19px;color:var(--navy);letter-spacing:.3px}
.upcoming{top:675px;height:205px}
.upcoming .sub{font-size:8.5px;font-weight:700;text-align:center;margin-top:8px;color:#222}
.upcoming .photo{width:154px;height:62px;margin:9px 0 0 5px;background:linear-gradient(180deg,#b8c9d6 0%,#c9c3b8 50%,#2c2d33 100%)}
.upcoming .meta{font-size:8px;line-height:11px;margin:12px 0 0 5px;color:#222}
.upcoming .meta + .meta{margin-top:9px}
.testimonials{top:904px;height:179px}
.testimonials .quote{position:relative;font-size:8.6px;line-height:13.5px;color:#222;margin-top:10px;text-indent:22px}
.testimonials .quote svg{position:absolute;left:-1px;top:-1px}
.testimonials .cite{font-size:8.5px;font-weight:700;font-style:italic;color:var(--navy);margin-top:11px}

/* footer */
.footer{left:0;top:1106px;width:806px;height:68px;background:var(--footer)}
.footer-info{left:70px;top:16px;font-size:9.4px;line-height:12.2px;color:#eee}
.footer-brand{left:398px;top:22px;display:flex;align-items:center;gap:5px}
.footer-brand .brand-mark{width:8px;height:8px}
.footer-brand .brand-name{font-size:11px;color:#f1f1f1}
.badges{left:521px;top:26px;display:flex;gap:6px;align-items:center}
.badge{height:27px;background:#f1f1f1}
.copyright{left:0;top:1174px;width:806px;height:26px;background:var(--footer-base);color:#ddd;font-size:8.5px;line-height:26px;text-align:center}
</style>
</head>
<body>

<header>
  <div class="abs brand">
    <span class="brand-mark"></span>
    <span class="brand-name">Brenn<br>Realty &amp; Auction LLC</span>
  </div>

  <div class="abs social">
    <span class="social-label">Social Media:</span>
    <span class="social-btn" style="background:#3b5a96" aria-label="Social link one"></span>
    <span class="social-btn" style="background:#4fb4e6" aria-label="Social link two"></span>
    <span class="social-btn" style="background:#c9322b" aria-label="Video channel link"></span>
  </div>

  <div class="abs contact">
    <svg width="12" height="12" viewBox="0 0 24 24"><path fill="#333" d="M6.6 10.8c1.4 2.8 3.8 5.1 6.6 6.6l2.2-2.2c.3-.3.7-.4 1-.2 1.1.4 2.3.6 3.6.6.6 0 1 .4 1 1V20c0 .6-.4 1-1 1C10.6 21 3 13.4 3 4c0-.6.4-1 1-1h3.5c.6 0 1 .4 1 1 0 1.3.2 2.5.6 3.6.1.3 0 .7-.2 1z"/></svg>
    <span>(615) 555 0142</span>
    <svg width="14" height="10" viewBox="0 0 14 10" style="margin-left:8px"><rect width="14" height="10" fill="#333"/><path d="M0 0l7 6 7-6" fill="none" stroke="#fff" stroke-width="1"/></svg>
    <span>info@brennrealty.com</span>
  </div>
</header>

<nav class="abs nav">
  <a>Home</a><span class="sep" style="margin:0 8px"></span>
  <a class="active">Current Auctions</a><span class="sep" style="margin:0 14px 0 12px"></span>
  <a>Past Auctions</a><span class="sep" style="margin:0 14px 0 14px"></span>
  <a>Referrals</a><span class="sep" style="margin:0 14px 0 14px"></span>
  <a>Why Auction</a><span class="sep" style="margin:0 14px 0 14px"></span>
  <a>About Us</a><span class="sep" style="margin:0 4px 0 6px"></span>
  <a>Contact Us</a>
</nav>

<section class="abs hero" role="img" aria-label="Photo of a two-storey suburban home with grey siding, front lawn and landscaped garden"></section>
<div class="abs tagline">Bid Smart With Brenn!</div>

<main>
  <h1 class="abs head welcome-title">Welcome to Brenn Realty &amp; Auction LLC</h1>
  <p class="abs welcome-text">simply dummy text of the printing and typesetting industry. Lorem Ipsum has been the industry's standard dummy text ever since the 1500s, when an unknown printer took a galley of type and scrambled it to make a type specimen book.</p>

  <h2 class="abs head section-title">Current Auctions</h2>

  <article class="abs card" style="top:573px">
    <div class="card-head">Vehicles * Tractors * Farm Machinery</div>
    <div class="card-photo" role="img" aria-label="Photo of a dark green colonial house"></div>
    <div class="card-btn"><svg width="10" height="10" viewBox="0 0 10 10"><circle cx="6" cy="4" r="3" fill="none" stroke="#fff" stroke-width="1.4"/><path d="M4 6L1 9" stroke="#fff" stroke-width="1.6"/></svg>Details</div>
    <div class="card-body">
      <div class="label">Selling To the Highest Bidder</div>
      <p>simply dummy text of the printing and typesetting industry. Lorem Ipsum has been the industry's.</p>
      <div class="label" style="margin-top:5px">Live On Site Auction</div>
      <div>Begins:&nbsp; Saturday, March 16, 2013 at 10:00 AM EDT</div>
      <div class="label" style="margin-top:6px">Location</div>
      <div>1918 Cedar Hollow, TN 37172</div>
    </div>
  </article>

  <article class="abs card" style="top:748px">
    <div class="card-head">Vehicles * Tractors * Farm Machinery</div>
    <div class="card-photo" role="img" aria-label="Photo of a dark green colonial house"></div>
    <div class="card-btn"><svg width="10" height="10" viewBox="0 0 10 10"><circle cx="6" cy="4" r="3" fill="none" stroke="#fff" stroke-width="1.4"/><path d="M4 6L1 9" stroke="#fff" stroke-width="1.6"/></svg>Details</div>
    <div class="card-body">
      <div class="label">Selling To the Highest Bidder</div>
      <p>simply dummy text of the printing and typesetting industry. Lorem Ipsum has been the industry's.</p>
      <div class="label" style="margin-top:5px">Live On Site Auction</div>
      <div>Begins:&nbsp; Saturday, March 16, 2013 at 10:00 AM EDT</div>
      <div class="label" style="margin-top:6px">Location</div>
      <div>1918 Cedar Hollow, TN 37172</div>
    </div>
  </article>

  <article class="abs card" style="top:926px">
    <div class="card-head">Vehicles * Tractors * Farm Machinery</div>
    <div class="card-photo" role="img" aria-label="Photo of a dark green colonial house"></div>
    <div class="card-btn"><svg width="10" height="10" viewBox="0 0 10 10"><circle cx="6" cy="4" r="3" fill="none" stroke="#fff" stroke-width="1.4"/><path d="M4 6L1 9" stroke="#fff" stroke-width="1.6"/></svg>Details</div>
    <div class="card-body">
      <div class="label">Selling To the Highest Bidder</div>
      <p>simply dummy text of the printing and typesetting industry. Lorem Ipsum has been the industry's.</p>
      <div class="label" style="margin-top:5px">Live On Site Auction</div>
      <div>Begins:&nbsp; Saturday, March 16, 2013 at 10:00 AM EDT</div>
      <div class="label" style="margin-top:6px">Location</div>
      <div>1918 Cedar Hollow, TN 37172</div>
    </div>
  </article>
</main>

<aside>
  <div class="abs email">
    <h3>Email Sign Up</h3>
    <p>Sign up for our free messages &amp; receive auction alerts.</p>
    <div class="email-form"><div class="email-input">Your Email Address</div><div class="email-go">GO</div></div>
  </div>

  <div class="abs register">
    <svg class="abs" style="left:10px;top:2px" width="48" height="66" viewBox="0 0 48 66">
      <path d="M32 12c0-8 8-10 12-8" fill="none" stroke="#2f3a2a" stroke-width="3" stroke-linecap="round"/>
      <rect x="4" y="16" width="32" height="48" rx="16" fill="#2f3a2a" transform="rotate(18 20 40)"/>
      <path d="M23 19l-4 14" stroke="#6a8f3c" stroke-width="2"/>
    </svg>
    <div class="abs big">Register</div>
    <div class="abs small">for Online Bidding</div>
  </div>

  <div class="abs widget upcoming">
    <h3>Upcoming Auctions</h3>
    <div class="sub">Multi Estate &amp; Consignment Auction</div>
    <div class="photo" role="img" aria-label="Photo of an agent in a suit standing before a house"></div>
    <div class="meta"><b>Start Date/ Time:</b> Saturday, April 13, 2013 At 10:00 Am</div>
    <div class="meta"><b>Location:</b> 1918 Cedar Hollow,&nbsp; 37172</div>
  </div>

  <div class="abs widget testimonials">
    <h3>Testimonials</h3>
    <p class="quote"><svg width="20" height="14" viewBox="0 0 20 14"><path d="M2 14c0-6 2-10 7-12v3c-2 1-3 3-3 4h3v5zM11 14c0-6 2-10 7-12v3c-2 1-3 3-3 4h3v5z" fill="#bbb"/></svg>Lorem Ipsum has been the industry's standard dummy text ever since the 1500s, when an unknown printer took a galley of type and scrambled it to make a type speci men book.It has a galley of type and scrambled a galley of type and scrambled survived not only five centuries.</p>
    <p class="cite">-Maren Holt</p>
  </div>
</aside>

<footer>
  <div class="abs footer">
    <div class="abs footer-info">Brenn Realty &amp; Auction LLC.<br>4870 Larkspur Pike, Franklin TN 37064<br>office@brennrealty.com<br>Phone: (615) 555 0187</div>
    <div class="abs footer-brand"><span class="brand-mark"></span><span class="brand-name">Brenn<br>Realty &amp; Auction LLC</span></div>
    <div class="abs badges">
      <span class="badge" style="width:56px"></span>
      <span class="badge" style="width:36px"></span>
      <span class="badge" style="width:73px"></span>
      <span class="badge" style="width:30px;height:34px"></span>
    </div>
  </div>
  <div class="abs copyright">Copyright © 2014 Brenn Realty &amp; Auction LLC. All Rights Reserved.</div>
</footer>

</body>
</html>
```